Nonprofit needs table front banner

Open Compass is a disability advocacy organization in Indiana. We are requesting a graphic design for a table front banner 28 inches high and 72 inches long. The banner must incorporate Open Compass’s logo, and the logos of our two web projects, ValeSpark and Quillbee. (See attached items.) We would also like the banner to incorporate our slogan, and the slogans of ValeSpark and Quillbee:

• ValeSpark slogan: “Finding Disability Services Online Can be Like Digging for a Needle in a Haystack. But with ValeSpark, Now You Have a Magnet.”

• Open Compass slogan: “Indiana’s Source for Disability News and Information”

• Quillbee slogan: “Where Workers with Disabilities and Inclusive Employers Connect!”

As Open Compass is the organization and ValeSpark and Quillbee are our projects, we would like Open Compass’s logo and slogan to be in the middle, and slightly more prominent. Also, as we are a disability organization, the banner should be designed with basic accessibility in mind. This means large text in a clear font, with good contrast between the text and the background. The text should be in a sans serif font that is clear and easy to read, with no italics or script fonts. There should not be a "busy" picture or pattern behind the text.

Industry/Entity Type

Non-Profit

Font styles to use
Sans Serif

Requirements
Must have
• The banner must incorporate Open Compass’s logo, and the logos of our two web projects, ValeSpark and Quillbee. (See attached items.) We would also like the banner to incorporate our slogan, and the slogans of ValeSpark and Quillbee:
• • ValeSpark slogan: “Finding Disability Services Online Can be Like Digging for a Needle in a Haystack. But with ValeSpark, Now You Have a Magnet.”
• • Open Compass slogan: “Indiana’s Source for Disability News and Information”
• • Quillbee slogan: “Where Workers with Disabilities and Inclusive Employers Connect!”
Nice to have
• As Open Compass is the organization and ValeSpark and Quillbee are our projects, we would like Open Compass’s logo and slogan to be in the middle, and slightly more prominent.
Should not have
• No italics or script fonts. There should not be a "busy" picture or pattern behind the text.

```html
<!DOCTYPE html>
<html lang="en">
<head>
<meta charset="utf-8">
<title>Open Compass – Table Front Banner</title>
<link rel="stylesheet" href="https://fonts.googleapis.com/css2?family=Source+Sans+3:wght@400;600&display=swap">
<style>
  :root {
    --brand-blue: #2c53a1;
    --text-blue: #2e55a0;
    --accent-pink: #f3a3a6;
    --accent-pink-soft: #f7c8ca;
    --paper: #ffffff;
    --on-blue: #ffffff;
  }
  * { margin: 0; padding: 0; box-sizing: border-box; }
  html, body { width: 1200px; height: 466px; overflow: hidden; background: var(--paper); }
  body { font-family: "Source Sans 3", "Myriad Pro", Arial, sans-serif; }

  .banner { position: relative; width: 1200px; height: 466px; background: var(--paper); overflow: hidden; }

  .streaks { position: absolute; inset: 0; width: 1200px; height: 328px; }
  .streak { fill: var(--accent-pink); }
  .streak--soft { fill: var(--accent-pink-soft); }

  .org-mark { position: absolute; left: 104px; top: 70px; width: 450px; height: 240px;
    display: flex; flex-direction: column; align-items: center; justify-content: center; gap: 22px; }
  .org-mark__dot { width: 130px; height: 130px; border-radius: 50%; background: var(--text-blue); }
  .org-mark__name { font-size: 58px; font-weight: 600; color: var(--text-blue); line-height: 1; }

  .org-slogan { position: absolute; right: 108px; top: 76px; text-align: right;
    color: var(--text-blue); font-weight: 400; font-size: 64px; line-height: 79px; letter-spacing: -0.3px; }

  .projects { position: absolute; left: 0; top: 328px; width: 1200px; height: 138px; background: var(--brand-blue); color: var(--on-blue); }

  .project-mark { position: absolute; display: flex; align-items: center; gap: 12px;
    font-size: 27px; font-weight: 400; color: var(--on-blue); line-height: 1; }
  .project-mark--valespark { left: 48px; top: 50px; }
  .project-mark--quillbee { left: 746px; top: 50px; }
  .project-mark__dot { width: 36px; height: 36px; border-radius: 50%; background: var(--on-blue); }
  .project-mark__square { width: 30px; height: 34px; background: var(--on-blue); }

  .project-slogan { position: absolute; font-size: 17.6px; line-height: 25px; color: var(--on-blue); }
  .project-slogan--valespark { left: 306px; top: 21px; width: 330px; }
  .project-slogan--quillbee { left: 962px; top: 33px; width: 230px; }
</style>
</head>
<body>
<main class="banner">
  <svg class="streaks" viewBox="0 0 1200 328" aria-hidden="true">
    <polygon class="streak" points="0,24 36,33 0,38"/>
    <polygon class="streak" points="0,56 110,74 0,92"/>
    <polygon class="streak" points="0,104 176,116 0,160"/>
    <polygon class="streak--soft" points="932,84 1200,0 1200,116"/>
    <polygon class="streak--soft" points="1032,148 1200,112 1200,160"/>
    <polygon class="streak--soft" points="1148,210 1200,200 1200,220"/>
  </svg>

  <div class="org-mark">
    <span class="org-mark__dot" aria-hidden="true"></span>
    <span class="org-mark__name">Open Compass</span>
  </div>

  <h1 class="org-slogan">Indiana’s Source for<br>Disability News<br>and Information</h1>

  <section class="projects">
    <div class="project-mark project-mark--valespark">
      <span class="project-mark__dot" aria-hidden="true"></span>
      <span>ValeSpark</span>
    </div>
    <p class="project-slogan project-slogan--valespark">Finding Disability Services Online Can be Like Digging for a Needle in a Haystack. But with ValeSpark, Now You Have a Magnet.</p>

    <div class="project-mark project-mark--quillbee">
      <span class="project-mark__square" aria-hidden="true"></span>
      <span>Quillbee</span>
    </div>
    <p class="project-slogan project-slogan--quillbee">Where Workers with Disabilities and Inclusive Employers Connect!</p>
  </section>
</main>
</body>
</html>
```